Wound Care Flyer

Looking for a Trifold brochure that is modern and has a high aesthetic. (Specialty services) Would like the colors to center around Black and Gold. Possibly updating the logo. Attached is the old brochure and a document about our services.

```html
<!DOCTYPE html>
<html lang="en">
<head>
<meta charset="utf-8">
<title>Cedarline Wounds – Trifold Brochure</title>
<link rel="stylesheet" href="https://fonts.googleapis.com/css2?family=Cinzel:wght@600;700&family=Montserrat:wght@400;600&display=swap">
<style>
  :root{
    --bg:#bdbdbd;
    --ink:#050505;
    --gold:#c9a45c;
    --gold-light:#ecd08e;
    --gold-deep:#8a6a2e;
    --white:#f3f0ea;
  }
  *{box-sizing:border-box;margin:0;padding:0}
  html,body{width:706px;height:1200px;overflow:hidden;background:var(--bg)}
  body{position:relative;font-family:"Montserrat",sans-serif;color:var(--white)}
  .spread{position:absolute;left:20px;width:666px;height:470px;background:var(--ink)}
  .spread--outside{top:90px}
  .spread--inside{top:620px}
  .spread-edge{position:absolute;left:0;bottom:0;width:100%;height:8px;background:var(--gold)}
  .art{position:absolute;left:0;top:0}
  .panel{position:absolute;top:0;width:222px;height:462px}
  .panel--1{left:0}.panel--2{left:222px}.panel--3{left:444px}
  .heading{font-weight:600;color:var(--gold);font-size:10.5px;line-height:1.2}
  .body-copy{font-size:7.4px;line-height:1.3;font-weight:400}
  .body-copy strong{font-weight:600}

  /* outside panel 1 */
  .intro{position:absolute;left:20px;top:204px;width:186px}
  .intro .heading{margin-bottom:7px}
  .intro .body-copy{font-size:7.8px}
  .intro .body-copy + .body-copy{margin-top:10px}

  /* contact panel */
  .contact{position:absolute;left:0;top:40px;width:222px;text-align:center}
  .contact-title{display:inline-block;font-family:"Cinzel",serif;font-weight:700;font-size:17px;
    color:var(--gold);border:2px solid var(--gold);border-radius:16px;padding:3px 14px 2px;letter-spacing:.5px}
  .contact-icon{display:block;margin:12px auto 3px;width:14px;height:14px}
  .contact-line{font-weight:600;font-size:15px;letter-spacing:.3px}
  .contact-mail{font-weight:600;font-size:8.6px}

  /* brand name */
  .brand-name{position:absolute;left:0;width:222px;text-align:center;font-weight:600;color:var(--gold);font-size:14px}
  .brand-name--contact{top:372px}
  .brand-name--cover{top:40px}

  .cover-title{position:absolute;left:0;top:352px;width:222px;text-align:center;font-family:"Cinzel",serif;line-height:1.05}
  .cover-title .kicker{display:block;color:var(--gold);font-size:12px;font-weight:600;margin-bottom:4px}
  .cover-title .main{display:block;color:var(--white);font-size:21px;font-weight:700}

  /* inside panel 1 */
  .story{position:absolute;left:22px;top:20px;width:186px;font-size:8px;line-height:1.26;font-weight:400}

  /* inside panel 2 */
  .services{position:absolute;left:14px;top:22px;width:198px}
  .services .heading{margin-bottom:6px}
  .service{position:relative;padding-left:28px;margin-top:11px}
  .service-icon{position:absolute;left:0;top:0;width:21px;height:21px}
  .service-title{font-weight:600;font-size:8px;margin-bottom:2px}
  .service .sub{font-size:6.6px;font-weight:600}
  .ticks{list-style:none;margin-top:4px}
  .ticks li{position:relative;padding-left:10px;font-size:7.2px;line-height:1.45}
  .ticks li::before{content:"";position:absolute;left:0;top:3px;width:6px;height:6px;border-radius:50%;background:var(--gold)}
  .note{margin-top:9px}

  /* inside panel 3 */
  .partner{position:absolute;left:18px;top:196px;width:192px}
  .partner .heading{margin-bottom:6px}
  .benefit{position:relative;padding-left:30px;margin-top:7px}
  .benefit-icon{position:absolute;left:0;top:1px;width:24px;height:24px}
  .benefit-title{font-weight:600;font-size:8px;margin-bottom:1px}
  .benefit .body-copy{font-size:7.1px;line-height:1.25}
</style>
</head>
<body>

<section class="spread spread--outside" aria-label="Brochure outside">
  <svg class="art" width="666" height="470" viewBox="0 0 666 470">
    <defs>
      <linearGradient id="clinicianTone" x1="0" y1="0" x2="1" y2="1">
        <stop offset="0" stop-color="#e3e1dc"/><stop offset=".6" stop-color="#a9b2b4"/><stop offset="1" stop-color="#3f8791"/>
      </linearGradient>
      <linearGradient id="officeTone" x1="0" y1="0" x2="1" y2="1">
        <stop offset="0" stop-color="#cfd3d6"/><stop offset=".55" stop-color="#7f9bb6"/><stop offset="1" stop-color="#e8e8e6"/>
      </linearGradient>
    </defs>
    <rect x="0" y="0" width="222" height="180" fill="url(#clinicianTone)" role="img" aria-label="Photo: clinician in a white coat taking notes on a tablet beside a patient"/>
    <rect x="444" y="95" width="222" height="218" fill="url(#officeTone)" role="img" aria-label="Photo: two smiling clinicians reviewing a laptop together"/>
    <rect x="222" y="313" width="444" height="2" fill="var(--gold)"/>
  </svg>
  <div class="spread-edge"></div>

  <div class="panel panel--1">
    <div class="intro">
      <h2 class="heading">Leaders in Mobile Advanced Wound Care.</h2>
      <p class="body-copy">We provide an additional layer of expertise by utilizing advanced the advanced technology of biological skin substitute grafts. We pride ourselves in working in close coordination with the patient's care team, including home health services and the primary care physician (PCP).<br>We ensure seamless integration without duplicating services prioritizing collaborative care, sharing detailed notes and working closely with the patient's home health team on days between visits.</p>
      <p class="body-copy">Serving the greater North Harbor area. (Ashford, Pine Ridge, Elmsworth, Brookvale, Linden, Marlow, Westgate, Fairhollow)</p>
    </div>
  </div>

  <div class="panel panel--2">
    <div class="contact">
      <h2 class="contact-title">CONTACT US</h2>
      <svg class="contact-icon" viewBox="0 0 24 24"><path fill="var(--gold)" d="M6.6 10.8a15 15 0 0 0 6.6 6.6l2.2-2.2c.3-.3.7-.4 1-.2 1.1.4 2.3.6 3.6.6.6 0 1 .4 1 1V20c0 .6-.4 1-1 1A17 17 0 0 1 3 4c0-.6.4-1 1-1h3.5c.6 0 1 .4 1 1 0 1.3.2 2.5.6 3.6.1.3 0 .7-.2 1z"/></svg>
      <p class="contact-line">(555) 014-2287</p>
      <svg class="contact-icon" viewBox="0 0 24 24"><path fill="var(--gold)" d="M6 2h12v6H6zM3 9h18c1 0 2 1 2 2v7h-4v4H5v-4H1v-7c0-1 1-2 2-2zm4 7v4h10v-4z"/></svg>
      <p class="contact-line">(555) 018-4403</p>
      <svg class="contact-icon" viewBox="0 0 24 24"><path fill="none" stroke="var(--gold)" stroke-width="1.8" d="M2 5h20v14H2zM2 5l10 8 10-8"/></svg>
      <p class="contact-mail">cedarlinewounds@example.com</p>
    </div>
    <p class="brand-name brand-name--contact">Cedarline Wounds</p>
  </div>

  <div class="panel panel--3">
    <p class="brand-name brand-name--cover">Cedarline Wounds</p>
    <h1 class="cover-title">
      <span class="kicker">Cedarline Wounds</span>
      <span class="main">Mobile<br>Wound Care</span>
    </h1>
  </div>
</section>

<section class="spread spread--inside" aria-label="Brochure inside">
  <svg class="art" width="666" height="470" viewBox="0 0 666 470">
    <defs>
      <linearGradient id="careTone" x1="0" y1="0" x2="1" y2="1">
        <stop offset="0" stop-color="#5d5f66"/><stop offset=".5" stop-color="#c9a890"/><stop offset="1" stop-color="#e8e2de"/>
      </linearGradient>
      <linearGradient id="visitTone" x1="0" y1="0" x2="1" y2="1">
        <stop offset="0" stop-color="#cfc6be"/><stop offset=".5" stop-color="#9b7560"/><stop offset="1" stop-color="#2a7da0"/>
      </linearGradient>
    </defs>
    <rect x="0" y="250" width="222" height="212" fill="url(#careTone)" role="img" aria-label="Photo: gloved hands examining a wound on a patient's lower leg"/>
    <rect x="0" y="244" width="222" height="2" fill="var(--gold)"/>
    <rect x="444" y="0" width="222" height="172" fill="url(#visitTone)" role="img" aria-label="Photo: smiling nurse holding an elderly patient's hands during a home visit"/>
  </svg>
  <div class="spread-edge"></div>

  <div class="panel panel--1">
    <p class="story">With a focus on convenience, expertise, and compassion, we bring the highest standard of wound care directly to the patient's home. Working side-by-side with the patient's physician, our team of experienced specialists utilize cutting-edge technology and personalized treatment plans to ensure optimal healing and comfort. From thorough wound assessments to advanced therapies and ongoing support, we prioritize the wellbeing of our patients everystep of the way. Whether it's managing chronic wounds, postsurgery recovery, we go above and beyond to provide comprehensive and compassionate care. With our concierge approach, we aim to make the healing journey as seamless and comfortable as possible, empowering our patients to live their best lives.</p>
  </div>

  <div class="panel panel--2">
    <div class="services">
      <h2 class="heading">Leaders in Mobile Advanced Wound Care.</h2>
      <p class="body-copy">We provide a complete wound management program for our patients that includes the use of advanced treatments, the creation of care plans, and coordination of care with other clinicians.<br><strong>Our comprehensive in-home wound care services include:</strong></p>

      <div class="service">
        <svg class="service-icon" viewBox="0 0 24 24"><circle cx="12" cy="12" r="11" fill="none" stroke="var(--gold)" stroke-width="1.3"/><rect x="7" y="6" width="8" height="11" fill="none" stroke="var(--gold)" stroke-width="1.2"/><circle cx="13" cy="13" r="2.5" fill="none" stroke="var(--gold)" stroke-width="1.2"/><path d="M15 15l3 3" stroke="var(--gold)" stroke-width="1.3"/></svg>
        <p class="service-title">Advanced Wound Assessment</p>
        <ul class="ticks"><li>Thorough evaluation of wound type, size, and stage to develop a tailored treatment plan.</li></ul>
      </div>

      <div class="service">
        <svg class="service-icon" viewBox="0 0 24 24"><circle cx="12" cy="12" r="11" fill="none" stroke="var(--gold)" stroke-width="1.3"/><path d="M7 17l7-7 2 2-7 7H7z M14 10l2-2 2 2-2 2" fill="none" stroke="var(--gold)" stroke-width="1.2"/></svg>
        <p class="service-title">Cutting-Edge Treatments</p>
        <p class="sub">Utilization of the latest technologies and techniques in wound care, including:</p>
        <ul class="ticks">
          <li>Compression</li>
          <li>Biologic Skin Substitutes</li>
          <li>Negative Pressure Wound Therapy</li>
          <li>Collagen and Advanced Dressings</li>
          <li>Surgical/ Trauma Wounds</li>
          <li>Venous/ Arterial Wounds</li>
          <li>Debridements</li>
        </ul>
      </div>

      <div class="service">
        <svg class="service-icon" viewBox="0 0 24 24"><circle cx="12" cy="12" r="11" fill="none" stroke="var(--gold)" stroke-width="1.3"/><rect x="7.5" y="6" width="9" height="12" rx="1" fill="none" stroke="var(--gold)" stroke-width="1.2"/><path d="M9.5 9.5h5M9.5 12h5M9.5 14.5h5" stroke="var(--gold)" stroke-width="1"/></svg>
        <p class="service-title">Personalized Care Plans</p>
        <p class="body-copy">Customized care plans designed to meet the specific needs of each patient, ensuring optimal healing. Coordination and direction of care for other caregivers and clinicians, including home health.</p>
        <p class="body-copy note">Patient and Caregiver Education<br>Providing education and support to patients and their caregivers to enhance understanding and promote self-care.</p>
      </div>
    </div>
  </div>

  <div class="panel panel--3">
    <div class="partner">
      <h2 class="heading">Partner with Cedarline Wounds:</h2>

      <div class="benefit">
        <svg class="benefit-icon" viewBox="0 0 24 24"><circle cx="12" cy="12" r="12" fill="var(--gold)"/><path d="M12 17l-5-5a2.8 2.8 0 0 1 5-3 2.8 2.8 0 0 1 5 3z" fill="var(--ink)"/></svg>
        <p class="benefit-title">Enhanced Patient Outcomes</p>
        <p class="body-copy">Our specialized expertise in advanced wound care leads to faster healing times and improved patient satisfaction.</p>
      </div>
      <div class="benefit">
        <svg class="benefit-icon" viewBox="0 0 24 24"><circle cx="12" cy="12" r="12" fill="var(--gold)"/><path d="M6 6h4l-4 4zM18 6v4l-4-4zM6 18v-4l4 4zM18 18h-4l4-4z" fill="var(--ink)"/><rect x="10" y="10" width="4" height="4" fill="var(--ink)"/></svg>
        <p class="benefit-title">Extended Reach</p>
        <p class="body-copy">Our in-home services allow your patients to receive high-quality care without the need for frequent visits, reducing the burden on your resources.</p>
      </div>
      <div class="benefit">
        <svg class="benefit-icon" viewBox="0 0 24 24"><circle cx="12" cy="12" r="12" fill="var(--gold)"/><circle cx="12" cy="12" r="5" fill="none" stroke="var(--ink)" stroke-width="2.2" stroke-dasharray="2.5 1.4"/><circle cx="12" cy="12" r="2" fill="var(--ink)"/></svg>
        <p class="benefit-title">Professional Integrity</p>
        <p class="body-copy">As a trusted partner, we uphold the highest standards of care and professionalism, reflecting positively on your clinic's reputation.</p>
      </div>
      <div class="benefit">
        <svg class="benefit-icon" viewBox="0 0 24 24"><circle cx="12" cy="12" r="12" fill="var(--gold)"/><path d="M6 7h12v8h-7l-3 3v-3H6z" fill="var(--ink)"/></svg>
        <p class="benefit-title">Enhanced Patient Outcomes</p>
        <p class="body-copy">We maintain open communication with referring clinics, ensuring a coordinated approach to patient care.</p>
      </div>
    </div>
  </div>
</section>

</body>
</html>
```